Webdesign für Immobilienmakler / Immobilienbüro
Zielgruppe
Das Unternehmen heißt LUMAR GmbH und kommt aus Heerbrugg in der Schweiz und will nun den Bereich Immobilien Vermarktung, Verkauf, Vermietung auf Süddeutschland erweitern.
Wir haben bis heute keine Webseite, weil unser Geschäft bis dato in der Schweiz durch Empfehlung, Mundpropaganda und Zeitunganzeigen funktioniert hat. Aber in Deutschland ist es ja ein Muß, was uns sicherlich auch den Einstieg erleichtern wird.
Aufgabenstellung
Wir benötigen eine Homepage für den Verkauf, Vermietung, Vermittlung von Immobilien für Privat und Gewerbe. Zu den Kategorien und der Gliederung haben wir keine bestimmte Vorstellung.
Hier hat der Designer freie Hand und wir freuen uns auf Ihren Vorschlag

```html
<!DOCTYPE html>
<html lang="de">
<head>
<meta charset="utf-8">
<title>LUMAR GmbH – Immobilien</title>
<link href="https://fonts.googleapis.com/css2?family=Open+Sans:wght@300;400;600;700&display=swap" rel="stylesheet">
<style>
:root{
  --dark:#262425;
  --dark-2:#1c1a1b;
  --black:#000;
  --red:#b5131f;
  --red-dark:#8f0e17;
  --text:#3a3a3a;
  --muted:#555;
  --white:#fff;
  --line:#d9d9d9;
}
*{box-sizing:border-box;margin:0;padding:0}
html,body{width:1200px;height:1170px;overflow:hidden;background:var(--white)}
body{font-family:"Open Sans",Arial,sans-serif;color:var(--text);position:relative}
.abs{position:absolute}

.site-header{position:absolute;left:0;top:0;width:1200px;height:129px;background:linear-gradient(#2e2c2d,#1f1d1e)}
.brand{left:214px;top:42px;font-size:31px;font-weight:700;color:var(--white);letter-spacing:-.3px}
.main-nav{right:218px;top:56px;display:flex;gap:33px}
.main-nav a{color:var(--white);text-decoration:none;font-size:17px}

.hero{left:214px;top:169px;width:768px;height:343px;display:flex;border:1px solid #ccc}
.hero-photo{width:481px;height:100%;background:linear-gradient(150deg,#ffffff 0%,#9fb6e6 25%,#3b5cc0 55%,#13246e 85%,#0a0f2c 100%)}
.hero-panel{flex:1;background:linear-gradient(#2a2829,#1a1819);color:#e8e8e8;padding:20px 26px;position:relative}
.hero-panel h1{font-size:20px;font-weight:700;color:var(--white);margin-bottom:13px}
.hero-panel .rule{height:1px;background:linear-gradient(90deg,transparent,#888,transparent);margin-bottom:13px}
.hero-panel p{font-size:12px;line-height:18.4px;font-weight:300}
.hero-panel .facts{margin-top:18px}
.hero-panel b{font-weight:700;color:var(--white)}
.hero-arrows{position:absolute;right:14px;bottom:12px;display:flex;gap:6px}
.hero-shadow{left:224px;top:512px;width:748px;height:26px;background:radial-gradient(ellipse at top,rgba(0,0,0,.22),transparent 70%)}

.intro{left:215px;top:562px;width:445px}
.section-title{font-size:19px;font-weight:300;color:#333}
.intro p{font-size:12px;line-height:17.6px;margin-top:24px;color:var(--muted)}
.intro p + p{margin-top:17.6px}

.listing-strip{left:214px;top:875px;width:462px;height:103px;background:linear-gradient(#fff,#eee);border-top:1px solid #ddd;box-shadow:0 3px 6px rgba(0,0,0,.15)}
.strip-btn{position:absolute;top:0;width:23px;height:103px;background:var(--red);display:flex;align-items:center;justify-content:center}
.strip-btn.prev{left:0}.strip-btn.next{right:0}
.listing{position:absolute;top:20px;display:flex;gap:9px;font-size:11.5px;line-height:18.4px;color:var(--muted)}
.listing .thumb{width:67px;height:66px;margin-top:0}
.listing .more{color:var(--red);font-weight:600}

.contact{left:697px;top:562px;width:285px}
.contact p{font-size:12px;line-height:17.6px;margin-top:22px;color:var(--muted)}
.cta{display:inline-flex;align-items:center;gap:12px;margin-top:20px;margin-left:-1px;height:28px;padding:0 12px;background:var(--red);color:var(--white);font-size:12.5px;font-weight:600;box-shadow:0 2px 3px rgba(0,0,0,.2)}

.search{left:695px;top:728px;width:287px;height:250px;background:var(--black);color:var(--white);padding:16px 17px}
.search h2{font-size:19px;font-weight:300;text-decoration:underline;text-underline-offset:3px}
.search label{display:block;font-size:11.5px;margin-top:18px}
.search .field{height:25px;background:var(--white);margin-top:12px}
.select-row{display:flex;gap:7px;margin-top:12px}
.select-row .field{margin:0;width:220px}
.drop-red{width:26px;height:25px;background:var(--red);display:flex;align-items:center;justify-content:center}
.small-row{display:flex;justify-content:space-between;font-size:11.5px;margin-top:13px}
.small-fields{display:flex;justify-content:space-between;margin-top:7px}
.small-fields div{width:56px;height:20px;background:var(--white);position:relative}

.site-footer{left:0;top:1031px;width:1200px;height:113px;background:var(--dark);color:#e4e4e4;font-size:12px}
.footer-info{position:absolute;left:215px;top:12px;line-height:18.4px}
.footer-info strong{display:block;font-weight:600;color:var(--white);margin-bottom:4px}
.footer-nav{position:absolute;right:218px;top:12px;display:flex;gap:16px;font-weight:600;color:var(--white)}
.copyright{left:0;top:1150px;width:1200px;text-align:center;font-size:11.5px;color:var(--muted)}
</style>
</head>
<body>
<header class="site-header">
  <div class="abs brand">LUMAR GmbH</div>
  <nav class="abs main-nav"><a href="#">Über uns</a><a href="#">Immobilien</a><a href="#">Kontakt</a><a href="#">Karriere</a></nav>
</header>

<section class="abs hero">
  <div class="hero-photo" role="img" aria-label="Modernes verglastes Bürogebäude vor blauem Himmel, gespiegelt im Wasser"></div>
  <div class="hero-panel">
    <h1>Bürogebäude in München</h1>
    <div class="rule"></div>
    <p>Lorem ipsum dolor sit amet, consectetuer adipiscing elit. Aenean commodo ligula eget dolor. Aenean massa. Cum sociis natoque penatibus et magnis dis parturient montes, nascetur ridiculus mus. Donec quam felis, ultricies nec, pellentesque eu, pretium quis, sem. Nulla consequat massa quis enim.</p>
    <p class="facts"><b>Größe:</b> 300m²<br><b>Baujahr:</b> 2010</p>
    <div class="hero-arrows">
      <svg width="8" height="13"><path d="M7 0v13L0 6.5z" fill="#fff"/></svg>
      <svg width="8" height="13"><path d="M1 0v13l7-6.5z" fill="#fff"/></svg>
    </div>
  </div>
</section>
<div class="abs hero-shadow"></div>

<section class="abs intro">
  <h2 class="section-title">Finden Sie Ihre Traum Immobilie!</h2>
  <p>Lorem ipsum dolor sit amet, consectetuer adipiscing elit. Aenean commodo ligula eget dolor. Aenean massa. Cum sociis natoque penatibus et magnis dis parturient montes, nascetur ridiculus mus. Donec quam felis, ultricies nec, pellentesque eu, pretium quis, sem. Nulla consequat massa quis enim. Donec pede justo, fringilla vel, aliquet nec, vulputate eget, arcu. In enim justo, rhoncus ut, imperdiet a, venenatis vitae, justo. Nullam dictum felis eu pede mollis pretium. Integer tincidunt.</p>
  <p>Cras dapibus. Vivamus elementum semper nisi. Aenean vulputate eleifend tellus. Aenean leo ligula, porttitor eu, consequat vitae, eleifend ac, enim. Aliquam lorem ante, dapibus in, viverra quis, feugiat a, tellus. Phasellus viverra nulla ut metus varius laoreet. Quisque rutrum. Aenean imperdiet. Etiam ultricies nisi vel augue.</p>
</section>

<section class="abs listing-strip">
  <div class="strip-btn prev"><svg width="15" height="15"><circle cx="7.5" cy="7.5" r="7.5" fill="#fff"/><path d="M9 4v7L5 7.5z" fill="#b5131f"/></svg></div>
  <div class="listing" style="left:38px">
    <div class="thumb" role="img" aria-label="Gelbes Einfamilienhaus mit Garten" style="background:linear-gradient(#8fb4e0 0%,#bcd3ee 35%,#e8c35a 55%,#7a8f4a 100%)"></div>
    <div>Art: Einfamilienhaus<br>Ort: Dresden<br>BJ: Mai 2008<br><span class="more">mehr...</span></div>
  </div>
  <div class="listing" style="left:234px">
    <div class="thumb" role="img" aria-label="Modernes weißes Mehrfamilienhaus" style="background:linear-gradient(#6f9bd6 0%,#c7d9ef 30%,#f2f2f2 55%,#8d8d80 100%)"></div>
    <div>Art: Mehrfamilienhaus<br>Ort: Köln<br>BJ: November 1996<br><span class="more">mehr...</span></div>
  </div>
  <div class="strip-btn next"><svg width="15" height="15"><circle cx="7.5" cy="7.5" r="7.5" fill="#fff"/><path d="M6 4v7l4-3.5z" fill="#b5131f"/></svg></div>
</section>

<section class="abs contact">
  <h2 class="section-title">Anfragen &nbsp;|&nbsp; Kontaktaufnahme</h2>
  <p>Sie erreichen uns unter der Nummer<br>0421 5538 2210 oder nutzen Sie ganz bequem unser Kontaktformular.</p>
  <span class="cta">zum Kontaktformular <svg width="7" height="12"><path d="M0 0v12l7-6z" fill="#fff"/></svg></span>
</section>

<section class="abs search">
  <h2>Immobiliensuche</h2>
  <label><b>Wo:</b> Ort, PLZ oder Straße</label>
  <div class="field"></div>
  <label><b>Was:</b> Eigentumswohnung, Haus etc.</label>
  <div class="select-row"><div class="field"></div><div class="drop-red"><svg width="12" height="7"><path d="M0 0h12L6 7z" fill="#fff"/></svg></div></div>
  <div class="small-row"><span>Preis bis</span><span>Zimmer ab:</span><span>Fläche ab:</span></div>
  <div class="small-fields"><div></div><div><svg class="abs" style="right:6px;top:7px" width="9" height="5"><path d="M0 0h9L4.5 5z" fill="#000"/></svg></div><div></div></div>
</section>

<footer class="abs site-footer">
  <div class="footer-info">
    <strong>LUMAR GmbH</strong>
    Musterstraße 1 &nbsp;|&nbsp; 00000 Musterstadt<br>
    Tel 0421 5538 2210 &nbsp;|&nbsp; Fax 0421 5538 2211<br>
    info@lumar.de &nbsp;|&nbsp; www.lumar.de
  </div>
  <nav class="footer-nav"><span>AGB</span><span>Kontakt</span><span>Impressum</span></nav>
</footer>
<div class="abs copyright">Copyright 2013. All Rights Reserved.</div>
</body>
</html>
```